Clinic for cellulit and fat removal

Name of clinic :
Velmora
- Body & Health (this has to be written on the site.)
I need CMS for me to be able to make changes myself.
A webpage for woman searching for a solution to remove fat and cellulit.
The owner is a brazilian woman in Denmark, and want her sense of aestetic shines thru the website.
There needs to be a slide show on the landing page showing big sliding pictures, of the clinic and and the treatments.
The Cryolipolysis, is a treatment freezing fat and cellulit, and this treatment will be the Attraction of the clinic.
Needs These pages in a horisontal fasion. (written in Danish)
Velmora
Behandlinger
- Cryolipolysis
- Trimcurve
- Lymfemassage
- Restalogic
- Radiant Pulse
Produkter
Priser
Kontakt
Clinic

```html
<!DOCTYPE html>
<html lang="da">
<head>
<meta charset="utf-8">
<title>Velmora – Behandlinger</title>
<link rel="stylesheet" href="https://fonts.googleapis.com/css2?family=Pacifico&family=Damion&family=Noto+Sans:wght@400&display=swap">
<style>
  :root {
    --pink: #b3307f;
    --mint: #7fcdb0;
    --mint-soft: #d6f6ea;
    --ink: #2b2b2b;
    --body-ink: #3a3a3a;
    --white: #ffffff;
    --line: #bfe8d8;
  }
  * { box-sizing: border-box; margin: 0; padding: 0; }
  html, body { width: 1200px; height: 675px; overflow: hidden; background: var(--white); }
  body { position: relative; font-family: "Noto Sans", Arial, sans-serif; color: var(--ink); }

  .sidebar { position: absolute; left: 0; top: 0; width: 200px; height: 675px; background: var(--white); z-index: 2; }
  .brand { position: absolute; left: 34px; top: 40px; }
  .brand-name { display: flex; align-items: center; gap: 8px; font-family: "Noto Sans", Arial, sans-serif; font-weight: 400; font-size: 28px; color: var(--ink); line-height: 1; }
  .brand-dot { width: 10px; height: 10px; border-radius: 50%; background: var(--mint); }
  .brand-tagline { margin: 10px 0 0 18px; font-family: "Noto Sans", Arial, sans-serif; font-weight: 400; font-size: 11px; letter-spacing: .6px; color: var(--ink); line-height: 1; }

  .nav { position: absolute; left: 0; top: 136px; width: 200px; list-style: none; border-top: 1px dashed var(--line); }
  .nav li { height: 46.5px; display: flex; align-items: center; padding-left: 30px; font-size: 10.5px; letter-spacing: .3px; border-bottom: 1px dashed var(--line); }
  .nav li.is-active { background: var(--mint-soft); border-right: 2px solid var(--mint); border-bottom-color: transparent; }

  .social { position: absolute; left: 34px; top: 616px; display: flex; align-items: center; gap: 22px; list-style: none; }
  .social li { width: 12px; height: 12px; border-radius: 50%; border: 1.5px solid var(--mint); }
  .social li.is-primary { width: 28px; height: 28px; border: 0; background: var(--mint); margin-right: -4px; }

  .columns { position: absolute; left: 200px; top: 0; width: 1000px; height: 675px; display: flex; }
  .treatment { position: relative; width: 200px; height: 675px; text-align: center; }
  .treatment-media { position: absolute; inset: 0; }
  .media-cryo { background: linear-gradient(180deg, #f6f0ea 0%, #f4eee9 40%, #f7ebe6 100%); }
  .media-plain { background: var(--white); }
  .media-lymf { background: linear-gradient(180deg, #fbf6f6 0%, #f8ecea 50%, #f6e6e3 100%); }
  .media-radiant { background: linear-gradient(180deg, #f6f3f1 0%, #f8f1ee 50%, #f7f4f3 100%); }

  .treatment-body { position: absolute; left: 0; right: 0; top: 245px; padding: 0 16px; }
  .treatment-title { font-family: "Damion", cursive; font-weight: 400; font-size: 21px; color: var(--ink); height: 26px; }
  .treatment-text { margin-top: 30px; font-size: 10.6px; line-height: 12.5px; color: var(--body-ink); letter-spacing: .2px; height: 64px; }
  .read-more { display: inline-block; margin-top: 28px; width: 75px; height: 31px; line-height: 29px; border: 1px solid var(--pink); border-radius: 2px; background: var(--white); color: var(--pink); font-size: 10.5px; text-decoration: none; }

  .page-title { position: absolute; left: 200px; right: 0; top: 22px; text-align: center; padding-left: 200px; font-family: "Pacifico", cursive; font-weight: 400; font-size: 42px; color: var(--pink); z-index: 3; }
  .footer-note { position: absolute; right: 21px; top: 632px; font-size: 8.8px; color: var(--ink); z-index: 3; }
</style>
</head>
<body>
  <aside class="sidebar">
    <div class="brand">
      <div class="brand-name"><span class="brand-dot"></span>Velmora</div>
      <div class="brand-tagline">Body &amp; Health</div>
    </div>
    <ul class="nav">
      <li>Velmora</li>
      <li class="is-active">Behandlinger</li>
      <li>Produkter</li>
      <li>Priser</li>
      <li>Kontakt</li>
    </ul>
    <ul class="social" aria-label="Sociale medier">
      <li class="is-primary"></li><li></li><li></li><li></li>
    </ul>
  </aside>

  <main class="columns">
    <section class="treatment">
      <div class="treatment-media media-cryo" role="img" aria-label="Faded photo of a cryolipolysis treatment at the clinic"></div>
      <div class="treatment-body">
        <h2 class="treatment-title">Cryolipolysis</h2>
        <p class="treatment-text">Lorem ipsum dolor sit amet, consectetuer adipiscing elit, sed diam nonummy nibh euismod tincidunt ut laoreet dolore magna aliquam erat volutpat.</p>
        <a class="read-more" href="#">Read More</a>
      </div>
    </section>
    <section class="treatment">
      <div class="treatment-media media-plain"></div>
      <div class="treatment-body">
        <h2 class="treatment-title">Trimcurve</h2>
        <p class="treatment-text">Duis autem vel eum iriure dolor in hendrerit in vulputate velit esse molestie consequat, vel illum dolore eu feugiat nulla facilisis at vero eros.</p>
        <a class="read-more" href="#">Read More</a>
      </div>
    </section>
    <section class="treatment">
      <div class="treatment-media media-lymf" role="img" aria-label="Faded photo of hands giving a lymphatic massage"></div>
      <div class="treatment-body">
        <h2 class="treatment-title">Lymfemassage</h2>
        <p class="treatment-text">Nam liber tempor cum soluta nobis eleifend option congue nihil imperdiet doming id quod mazim placerat facer possim assum.</p>
        <a class="read-more" href="#">Read More</a>
      </div>
    </section>
    <section class="treatment">
      <div class="treatment-media media-plain"></div>
      <div class="treatment-body">
        <h2 class="treatment-title">Restalogic</h2>
        <p class="treatment-text">Investigationes demonstrave lectores legere me lius quod ii legunt saepius. Claritas est etiam processus dynamicus, qui sequitur mutationem.</p>
        <a class="read-more" href="#">Read More</a>
      </div>
    </section>
    <section class="treatment">
      <div class="treatment-media media-radiant" role="img" aria-label="Faded photo of a relaxed client at the clinic"></div>
      <div class="treatment-body">
        <h2 class="treatment-title">Radiant Pulse</h2>
        <p class="treatment-text">Mirum est notare quam littera gothica, quam nunc putamus parum claram, anteposuerit litterarum formas humanitatis per seacula quarta decima et.</p>
        <a class="read-more" href="#">Read More</a>
      </div>
    </section>
  </main>

  <h1 class="page-title">Behandlinger</h1>
  <p class="footer-note">© Copyright Velmora 2017</p>
</body>
</html>
```